Torvane PT Business Card

I need the card to be bright/bold colours to stand out amongst others.
It needs to have my company logo.
I was not interested in pictures etc just a layout that attracts attention.

I have attached my old design which is very plain. I also needed change the contact details. And my description changed to Personal Trainer
Phone 0427391058
Facebook Torvane PT
No email address please, no street address.
And only Torvane PT (Please remove anything to do with Torvane Supplements)

```html
<!DOCTYPE html>
<html lang="en">
<head>
<meta charset="utf-8">
<title>Torvane PT Business Card</title>
<link href="https://fonts.googleapis.com/css2?family=Exo+2:wght@400;700;800&display=swap" rel="stylesheet">
<style>
  :root {
    --backdrop: #4a4a4a;
    --card: #ffffff;
    --brand-blue: #1a8ad0;
    --soft-blue: #8fb3e3;
    --soft-yellow: #fdeea0;
    --ink-grey: #5a5a5a;
    --rule-grey: #7a7a7a;
  }
  html, body {
    margin: 0;
    padding: 0;
    width: 1200px;
    height: 900px;
    overflow: hidden;
    background: var(--backdrop);
    font-family: "Exo 2", sans-serif;
  }
  .business-card {
    position: absolute;
    left: 100px;
    top: 165px;
    width: 1000px;
    height: 570px;
    background: var(--card);
    border-radius: 48px;
    overflow: hidden;
  }
  .brand {
    position: absolute;
    left: 330px;
    top: 120px;
    width: 360px;
    text-align: center;
  }
  .brand-name {
    margin: 0;
    font-weight: 800;
    font-size: 62px;
    letter-spacing: 1px;
    line-height: 1;
    color: var(--brand-blue);
    text-transform: uppercase;
  }
  .brand-rule {
    display: block;
    height: 2px;
    margin: 16px auto 0;
    width: 340px;
    background: var(--brand-blue);
  }
  .divider {
    position: absolute;
    left: 420px;
    top: 330px;
    width: 520px;
    height: 2px;
    background: var(--rule-grey);
  }
  .accent-mark {
    position: absolute;
    right: 70px;
    top: 360px;
    width: 150px;
    height: 150px;
  }
  .person {
    position: absolute;
    left: 90px;
    top: 300px;
  }
  .person-name {
    margin: 0;
    font-weight: 700;
    font-size: 40px;
    color: var(--brand-blue);
    letter-spacing: 1px;
    line-height: 1;
  }
  .person-role {
    margin: 6px 0 0;
    font-size: 21px;
    color: var(--ink-grey);
    letter-spacing: 1px;
  }
  .contact-list {
    position: absolute;
    left: 90px;
    top: 420px;
    margin: 0;
    padding: 0;
    list-style: none;
  }
  .contact-item {
    display: flex;
    align-items: center;
    gap: 18px;
    font-size: 25px;
    color: var(--ink-grey);
    letter-spacing: 1px;
    margin-bottom: 14px;
  }
  .contact-icon {
    width: 28px;
    height: 28px;
    flex: none;
  }
</style>
</head>
<body>
  <main class="business-card">
    <header class="brand">
      <h1 class="brand-name">Torvane PT</h1>
      <span class="brand-rule"></span>
    </header>

    <div class="divider"></div>

    <svg class="accent-mark" viewBox="0 0 150 150" aria-hidden="true">
      <circle cx="75" cy="75" r="70" fill="var(--soft-blue)" opacity="0.35"/>
    </svg>

    <section class="person">
      <h2 class="person-name">DANA REYES</h2>
      <p class="person-role">PERSONAL TRAINER</p>
    </section>

    <ul class="contact-list">
      <li class="contact-item">
        <svg class="contact-icon" viewBox="0 0 28 28" aria-label="Phone">
          <rect width="28" height="28" rx="6" fill="var(--brand-blue)"/>
          <path d="M9 7c1 0 2 2.5 2 3.2 0 .8-1.3 1.2-1.2 2 .5 2 3 4.6 5 5 .8.1 1.2-1.2 2-1.2.7 0 3.2 1 3.2 2 0 1.5-1.5 3-3.2 3C11 21 7 17 7 10.8 7 9 7.8 7 9 7z" fill="#fff"/>
        </svg>
        <span>0427391058</span>
      </li>
      <li class="contact-item">
        <svg class="contact-icon" viewBox="0 0 28 28" aria-hidden="true">
          <rect width="28" height="28" rx="6" fill="var(--brand-blue)"/>
        </svg>
        <span>Torvane PT</span>
      </li>
    </ul>
  </main>
</body>
</html>
```